Web Design Project: Facility Management company

Hi! We need a new website.

Our current website: http://www.brantel-group.ru/ and we don-t like it. =)
The structure of our company has changed and now we don't need "cleaning" and "engeneering" on this site.

We are facility management company in Russia. So we provide integrated service solutions specific to industrial services: maintenance, repair, etc. of engineering systems.
More services:
Energy planning
Automation
Audit
Statements with regulators
Video surveillance
Central heating
Security systems
Welding
Management of subcontractors
Electrical installation and service needs
Reception
Catering

Visitors:
* Managers in the field of commercial real estate
* Chief engineers
* TOP managers of large companies, malls, factories...
+ their subordinates
* Small% of applicants.

Here you can see some websites/patterns we liked:
http://www.kvelmort.ru/ (This is our competitor’s site, so our site shouldn’t be an exact copy))))
http://www.orbitask.ru/
http://www.layoutpinery.com/demo/24296.html
http://www.layoutpinery.com/website-templates/10145.html

Style:
Light, hi-tech/minimalizm, the color palette should be based on the original site colors (Green + black + white). http://www.brantel-group.ru/

Estimated sitemap:
1. Home
2. About Us
3. Company's policy
4. History + Achievements.
5. Certificates
6. Map of presence (Here you can use sample map in file "our projects")
7. Services
8. Portfolio
9. News or blog
10. Jobs
11. Contacts - with the feedback form (or the function "call to order")
12. English

Need a design pages: main page, page 404. The rest of the page could be created by general pattern.

Logo, navigation bar and contacts should be visible on all pages of a site.
Flash animation elements and buttons, etc. - not needed.

* We need to develop 3 websites, so we are looking for a long term cooperation.
Looking forward to your creativity =)

Must Have:
Clear, intuitive structure of web pages.
In the center - of pictures reflecting our main services (industrial theme). May be in rotation.
BUT! This banner (central picture) should not be a huge one =)
All relevant information should be visible at once without scrolling.

A possibility to place media files (presentations, video ...) and 2 banner links on the main page.

Font should be available in Cyrillic.
Updates

IMPORTANT!

Please notice that in thisdesign we don't need "cleaning" and "engeneering" on this site.

So don't use old block of 4pictures from our current website. We don't need it anymore. 

Thestructure of our company has changed and now we need some links (may be banners,may be something else) to our future cleaning website as well as engeneeringwebsite.
It should look like seperate (partner) companies, not like our sevices.

Regards, Vera.

Please don't forget that we need bilingual site.

So define language changing tool in your designs.

Industry/Entity Type

Industrial

```html
<!DOCTYPE html>
<html lang="en">
<head>
<meta charset="utf-8">
<title>Kestrova Service — Facility Management</title>
<link rel="stylesheet" href="https://fonts.googleapis.com/css2?family=Arimo:wght@400;700&display=swap">
<style>
  :root {
    --backdrop-dark: #2f4a0c;
    --backdrop-mid: #5d8a1c;
    --backdrop-light: #a9d45a;
    --green: #7da528;
    --green-dark: #5f8a17;
    --green-soft: #86ac3a;
    --ink: #222;
    --text: #666;
    --muted: #8a8a8a;
    --line: #dcdcdc;
    --panel: #e2e2e2;
    --panel-deep: #d6d6d6;
    --white: #fff;
    --footer-text: #1d2a08;
  }
  * { box-sizing: border-box; margin: 0; padding: 0; }
  html, body { width: 1200px; height: 960px; overflow: hidden; }
  body {
    font-family: "Arimo", Arial, sans-serif;
    position: relative;
    background:
      radial-gradient(ellipse 260px 340px at 90px 300px, var(--backdrop-light), transparent 70%),
      radial-gradient(ellipse 300px 260px at 1120px 760px, var(--backdrop-mid), transparent 70%),
      radial-gradient(ellipse 240px 300px at 1100px 250px, #4a6f14, transparent 70%),
      radial-gradient(ellipse 380px 200px at 600px 930px, #6f9b26, transparent 70%),
      var(--backdrop-dark);
  }
  .abs { position: absolute; }
  a { color: inherit; text-decoration: none; }
  h2, h3, h4 { font-weight: 400; }

  .lang-bar { top: 20px; left: 780px; display: flex; font-size: 10px; color: var(--green-soft); }
  .lang-bar a { padding: 0 11px; border-left: 1px solid rgba(255,255,255,.15); }
  .lang-bar a:first-child { border-left: 0; }
  .lang-bar a.current { color: var(--white); text-decoration: underline; }

  .page {
    left: 192px; top: 40px; width: 816px; height: 795px;
    background: linear-gradient(#fff 0, #fff 100px, #ececec 118px, #f8f8f8 140px, #fff 200px, #fff 320px, #ececec 322px, #f6f6f6 420px, #fafafa 560px, #efefef 795px);
  }
  .brand { left: 31px; top: 27px; display: flex; align-items: center; gap: 10px; }
  .brand-mark { width: 22px; height: 22px; background: var(--green); }
  .brand-name { font-size: 22px; letter-spacing: 3px; color: var(--ink); font-weight: 400; }

  .main-nav { left: 336px; top: 52px; width: 448px; height: 20px; border-bottom: 3px solid #e6e6e6; display: flex; justify-content: space-between; font-size: 11.5px; color: #555; padding: 0 5px; }
  .main-nav a { padding-bottom: 6px; }
  .main-nav a.home { color: var(--green); }
  .main-nav a.active { color: var(--ink); border-bottom: 3px solid var(--green); margin-bottom: -3px; }

  .slider { left: 33px; top: 121px; width: 493px; height: 180px; border-radius: 3px; background: linear-gradient(100deg, #3f4a5e 0%, #8b96ad 35%, #b8c0d4 55%, #6f7f96 75%, #2d3b50 100%); }
  .slider-arrow { top: 74px; width: 32px; height: 32px; border-radius: 50%; border: 3px solid rgba(255,255,255,.55); }
  .slider-arrow svg { display: block; margin: 6px auto; }
  .slider-dots { left: 227px; bottom: 12px; display: flex; gap: 4px; }
  .slider-dots span { width: 4px; height: 4px; border-radius: 50%; background: rgba(255,255,255,.5); }
  .slider-dots span:first-child { background: #fff; }

  .contact-title { left: 575px; top: 124px; font-size: 13px; color: var(--green-soft); }
  .field { left: 560px; width: 224px; background: var(--panel); border-radius: 3px; font-size: 9px; color: var(--muted); padding: 11px 15px; }
  .field-mail { top: 146px; height: 31px; }
  .field-message { top: 185px; height: 72px; }
  .send-btn { left: 721px; top: 228px; width: 57px; height: 24px; background: var(--green); color: #fff; font-size: 10px; font-weight: 700; border-radius: 3px; text-align: center; line-height: 24px; }
  .call-line { left: 575px; top: 274px; font-size: 12.5px; color: var(--green); }
  .call-line b { font-size: 16px; }

  .section-title { font-size: 14px; color: var(--green-soft); }
  .rule { height: 1px; background: var(--line); }
  .about-title { left: 55px; top: 338px; }
  .about-rule { left: 33px; top: 369px; width: 495px; }
  .about-text { left: 55px; top: 389px; width: 440px; font-size: 9px; line-height: 14.4px; color: var(--text); }
  .about-text p + p { margin-top: 14px; }
  .about-text em { color: var(--green); font-weight: 700; text-decoration: underline; }

  .side-box { left: 560px; width: 224px; background: var(--panel); border-radius: 3px; }
  .company-box { top: 333px; height: 178px; }
  .side-title { left: 14px; top: 12px; font-size: 13px; color: var(--green-soft); }
  .side-rule { left: 8px; top: 36px; width: 208px; background: #cfcfcf; }
  .side-links { left: 14px; top: 52px; list-style: none; font-size: 11px; color: #555; }
  .side-links li { height: 24px; }
  .side-links li.current { color: var(--green-dark); font-weight: 700; text-decoration: underline; }

  .news-title { left: 55px; top: 553px; font-size: 11px; font-weight: 700; color: var(--green); }
  .news-rule { left: 33px; top: 579px; width: 495px; }
  .news-card { top: 600px; width: 216px; }
  .news-photo { width: 216px; height: 63px; border-radius: 4px; }
  .news-photo.one { background: linear-gradient(90deg, #223a66, #5d7fb8 40%, #9fb5d6 60%, #4d5f78); }
  .news-photo.two { background: linear-gradient(90deg, #4f6e95, #9cb3cf 45%, #c9d6e5 60%, #5a6f8a); }
  .news-head { margin-top: 13px; font-size: 11px; font-weight: 700; color: var(--green); line-height: 14px; }
  .news-date { font-size: 9px; font-weight: 700; color: #555; margin-top: 2px; }
  .news-body { font-size: 9px; color: var(--text); line-height: 14px; margin-top: 3px; }

  .where-box { top: 545px; height: 226px; }
  .city-select { left: 8px; top: 44px; width: 208px; height: 31px; background: var(--panel-deep); border-radius: 3px; font-size: 9.5px; color: #444; padding: 11px 15px; }
  .city-select svg { position: absolute; right: 12px; top: 11px; }
  .map-area { left: 8px; top: 85px; width: 208px; height: 127px; border: 2px solid #fff; border-radius: 3px; background: linear-gradient(120deg, #f2d9a8, #f6c46b 45%, #cfe0ef 55%, #f0d8a8); }

  .footer-links { left: 247px; top: 857px; font-size: 10.5px; color: var(--footer-text); line-height: 17px; }
  .footer-links .sep { margin: 0 6px; }
  .footer-links .current { color: #fff; text-decoration: underline; }
  .copyright { right: 225px; top: 857px; font-size: 10.5px; color: var(--footer-text); }
  .copyright b { color: #fff; font-weight: 400; }
</style>
</head>
<body>
  <nav class="lang-bar abs">
    <a href="#">English</a><a href="#">News</a><a href="#" class="current">Jobs</a><a href="#">Contact</a>
  </nav>

  <main class="page abs">
    <div class="brand abs"><span class="brand-mark"></span><span class="brand-name">KESTROVA SERVICE</span></div>

    <nav class="main-nav abs">
      <a href="#" class="home">Home</a><a href="#">About Us</a><a href="#">History &amp; Achievements</a><a href="#" class="active">Certificates</a><a href="#">Services</a><a href="#">Portfolio</a>
    </nav>

    <div class="slider abs" role="img" aria-label="Rotating banner: glass office towers seen from below">
      <span class="slider-arrow abs" style="left:31px"><svg width="12" height="14" viewBox="0 0 12 14"><path d="M9 1 3 7l6 6" fill="none" stroke="rgba(255,255,255,.7)" stroke-width="3"/></svg></span>
      <span class="slider-arrow abs" style="left:430px"><svg width="12" height="14" viewBox="0 0 12 14"><path d="m3 1 6 6-6 6" fill="none" stroke="rgba(255,255,255,.7)" stroke-width="3"/></svg></span>
      <div class="slider-dots abs"><span></span><span></span><span></span><span></span><span></span></div>
    </div>

    <h3 class="contact-title abs">Drop us a line..</h3>
    <div class="field field-mail abs">Your e-mail</div>
    <div class="field field-message abs">Your message</div>
    <a class="send-btn abs" href="#">Send</a>
    <p class="call-line abs">Or call us at <b>+7 812 555 0142</b></p>

    <h2 class="section-title about-title abs">About Us</h2>
    <div class="rule about-rule abs"></div>
    <div class="about-text abs">
      <p>We work next to you already for more than 8 years. Once we became one of the first companies, which decided to develop an integrated facility management of real estate in Russia. Today more than 500 professionals are <em>employed with us</em>, there are dozens of projects in the business portfolio: from small bank branch to super-regional shopping centre.</p>
      <p>While creating the company from the scratch, we set the goal for ourselves: to receive the invaluable knowledge: what our customer wants. Now we can tell with confidence that, at least, we have approached your aspirations and we are ready to listen to you to establish a mutually beneficial business together.</p>
    </div>

    <aside class="side-box company-box abs">
      <h3 class="side-title abs">Company</h3>
      <div class="rule side-rule abs"></div>
      <ul class="side-links abs">
        <li class="current">About our company</li><li>Background</li><li>Why us?</li><li>Chosen by</li><li>Our team</li>
      </ul>
    </aside>

    <h3 class="news-title abs">Latest news</h3>
    <div class="rule news-rule abs"></div>
    <article class="news-card abs" style="left:48px">
      <div class="news-photo one" role="img" aria-label="Photo of office skyscrapers against blue sky"></div>
      <h4 class="news-head">Lorem ipsum dolor sit amet</h4>
      <p class="news-date">[ 11.9.2012 ]</p>
      <p class="news-body">Consectetur adipiscing elit. Sed est ante, sagittis sit amet sollicitudin at, sagittis ut lacus. Nullam at risus est, ut pretium ligula.</p>
    </article>
    <article class="news-card abs" style="left:295px">
      <div class="news-photo two" role="img" aria-label="Photo of high-rise buildings and a street lamp"></div>
      <h4 class="news-head">Morbi tincidunt, arcu eget aliquam adipiscing</h4>
      <p class="news-date">[ 29.7.2012 ]</p>
      <p class="news-body">Sed nibh diam, accumsan quis egestas vitae, iaculis vel erat. Vestibulum nunc est, feugiat eu mollis sed, blandit id mi.</p>
    </article>

    <aside class="side-box where-box abs">
      <h3 class="side-title abs">Where you can find us?</h3>
      <div class="rule side-rule abs"></div>
      <div class="city-select abs">St. Petersburg
        <svg width="12" height="8" viewBox="0 0 12 8"><path d="m1 1 5 5 5-5" fill="none" stroke="#aaa" stroke-width="2.5"/></svg>
      </div>
      <div class="map-area abs" role="img" aria-label="Street map of the office location in St. Petersburg with a marker"></div>
    </aside>
  </main>

  <footer>
    <p class="footer-links abs">
      Company<span class="sep">|</span>Chosen by<span class="sep">|</span>Our team<span class="sep">|</span><span class="current">Contact us</span><span class="sep">|</span>Integrated facility management<br>
      Technical maintenance of engineering systems<span class="sep">|</span>Professional cleaning<span class="sep">|</span>Civil engineering
    </p>
    <p class="copyright abs">Copyright © 2012 <b>Kestrova</b></p>
  </footer>
</body>
</html>
```